Medical Billing - Professional Marketing Flier

We are needing help designing a clean and professional looking easy to read marketing flier for a medical billing practice. The text needs to be large enough to print. We are looking for a 5.5 x 8.5 design that we can edit the text as needed. I have included our logo and what we initially want it to say. Please keep in mind, we also want our logo and contact details on the flier. Let me know if you have any questions.

```html
<!DOCTYPE html>
<html lang="en">
<head>
<meta charset="utf-8">
<title>Vega Medical Billing – Flier</title>
<link href="https://fonts.googleapis.com/css2?family=Poppins:wght@400;500;600&display=swap" rel="stylesheet">
<style>
  :root{
    --navy:#1c3f8f;
    --sky:#149ad6;
    --violet:#7a5caf;
    --pink:#cf5fa6;
    --ink:#1c1c1c;
    --paper:#ffffff;
    --backdrop:#d6d6d6;
  }
  *{margin:0;padding:0;box-sizing:border-box}
  html,body{width:960px;height:1200px;overflow:hidden;background:var(--backdrop)}
  body{font-family:"Poppins",sans-serif;color:var(--ink)}
  .flier{
    position:absolute;left:92px;top:0;width:724px;height:1118px;
    background:var(--paper);overflow:hidden;
    transform:scale(1.0733);transform-origin:top left;
  }
  .shapes{position:absolute;inset:0;width:724px;height:1118px}
  .brand{position:absolute;left:36px;top:88px;width:290px;text-align:center;color:var(--violet);font-weight:500}
  .brand-name{display:block;font-size:70px;line-height:1;letter-spacing:4px}
  .brand-sub{display:block;font-size:15px;letter-spacing:5px;margin-top:8px}
  .band{position:absolute;height:46px;color:#fff;font-weight:600;font-size:30px;line-height:46px;letter-spacing:.3px}
  .band--billing{left:0;top:219px;width:405px;padding-left:25px;background:linear-gradient(90deg,var(--navy),var(--sky))}
  .band--aging{left:0;top:528px;width:330px;padding-left:33px;background:linear-gradient(90deg,var(--violet),var(--pink))}
  .band--cred{left:365px;top:528px;width:359px;padding-left:18px;background:linear-gradient(90deg,var(--navy),var(--sky))}
  .band--contact{left:330px;top:832px;width:394px;padding-left:53px;background:linear-gradient(90deg,var(--violet),var(--pink))}
  .copy{position:absolute;font-size:14.2px;line-height:17.5px}
  .copy--billing{left:26px;top:282px;width:285px}
  .copy--aging{left:26px;top:582px;width:285px}
  .copy--cred{left:383px;top:582px;width:285px}
  .copy--contact{left:383px;top:904px;width:322px}
  .address{
    position:absolute;left:26px;top:960px;color:#fff;font-weight:500;font-style:normal;
    font-size:14.2px;line-height:18px;white-space:nowrap
  }
</style>
</head>
<body>
<main class="flier">
  <svg class="shapes" viewBox="0 0 724 1118">
    <defs>
      <linearGradient id="grad-violet" x1="0" y1="1" x2="1" y2="0">
        <stop offset="0" stop-color="#7a5caf"/><stop offset="1" stop-color="#cf5fa6"/>
      </linearGradient>
      <linearGradient id="grad-blue" x1="0" y1="0" x2="1" y2="0">
        <stop offset="0" stop-color="#1c3f8f"/><stop offset="1" stop-color="#149ad6"/>
      </linearGradient>
      <linearGradient id="grad-photo" x1="0" y1="0" x2="1" y2="1">
        <stop offset="0" stop-color="#e9eef3"/><stop offset="1" stop-color="#8fc3e6"/>
      </linearGradient>
      <radialGradient id="grad-sparkle">
        <stop offset="0" stop-color="#d9a6d4" stop-opacity=".55"/><stop offset="1" stop-color="#9fc7e6" stop-opacity="0"/>
      </radialGradient>
    </defs>
    <polygon class="accent-chevron" fill="url(#grad-violet)" points="376,0 440,125 312,398 583,262 724,345 724,0"/>
    <polygon class="accent-corner" fill="url(#grad-blue)" points="583,0 724,0 724,345 583,262"/>
    <polygon class="photo-area" role="img" aria-label="Photo of a clinician in scrubs writing on a clipboard"
      fill="url(#grad-photo)" points="400,0 463,125 383,328 583,262 724,330 724,0"/>
    <ellipse class="sparkle-area" role="img" aria-label="Decorative star cluster" cx="540" cy="420" rx="180" ry="80" fill="url(#grad-sparkle)"/>
    <path class="accent-lower" fill="url(#grad-violet)"
      d="M0,795 L130,862 Q155,875 190,862 L382,772 L308,940 Q286,990 312,1045 L332,1118 L0,1118 Z"/>
    <ellipse class="sparkle-area" role="img" aria-label="Decorative stars" cx="160" cy="815" rx="55" ry="25" fill="url(#grad-sparkle)"/>
    <rect class="footer-strip" x="310" y="1086" width="414" height="32" fill="url(#grad-blue)"/>
  </svg>

  <div class="brand">
    <span class="brand-name">VEGA</span>
    <span class="brand-sub">MEDICAL BILLING</span>
  </div>

  <h2 class="band band--billing">MEDICAL BILLING</h2>
  <p class="copy copy--billing">Would you prefer to spend time focusing on your clients and running your practice rather than trying to stay up to speed with the constantly changing medical billing rules and regulations? Let us help you by managing your medical billing and dealing with the insurance companies on your behalf! We work with you to tailor the entire medical billing process to suit your practices needs while making it as smooth and painless as possible.</p>

  <h2 class="band band--aging">AGING</h2>
  <p class="copy copy--aging">Are you leaving money on the table? Are you able to do the follow-through needed to keep your aging in check and more money flowing into your practice? Are you uncertain about how to get insurance to pay on claims that should be covered but for some reason they decided not to? We can clean up your aging, reduce the amount of time it takes for claims to pay out, and we can keep your aging to a minimum.</p>

  <h2 class="band band--cred">CREDENTIALING</h2>
  <p class="copy copy--cred">Are you wanting to get contracted with insurance companies but aren’t sure how to go about it? Are you wanting to expand your client base by having the option to bill insurance? Let us take the confusion out of what can seem like a daunting task! We can get you and your practitioners contracted with the insurance companies of your choice and help you navigate through the process every step of the way!</p>

  <h2 class="band band--contact">CONTACT US</h2>
  <p class="copy copy--contact">If any of these processes are something you would like our help with or to consult with us on, please email us or give us a call! We specialize in billing and contracting for Nutritionists and Dietitians. We would love to help you expand your business and take the pain and frustration out of billing so you can focus on your clients.</p>

  <address class="address">Address: PO Box 418 Cedar Falls,<br>WA 98100<br>Phone: 425-555-0172<br>Email:<br>admin@vegamedicalbilling.com</address>
</main>
</body>
</html>
```